QZN Supplements needs a label designer for supplement company

Looking for an on going label designer for my supplement company. I have three products that will need designs. I'm about to launch my sleep supplement called Velmora Rest and that's the first design needed.
I would like all designs to be somewhat simple, not overstated and uniformed so that when you look at all of the labels of the different supplements they are similar and you can tell it's the same brand.
Please see attached sample pictures below as ideas.
Updates

The brand is QZN supplements, logo file has been provided. The supplement is called Velmora Rest. It is a liquid supplement that is a 32/33 ounce white bottle. Die lines and measurements will be provided. Here's text for wording ideas: Wording: Natural Sleep Aid Reset your circadian rhythm. May help you: Fall asleep faster. Get a deeper more restful sleep. Boost Immune System Remember your dreams. Protect your brain and flush toxins. Wake up feeling refreshed. Non-gmo Gluten Free Sugar Free Vegan Manufactured in cGMP factory Manufactured in USA

Target Market(s)

Health and wellness/supplement industry for regular people not hardcore gym goers. My supplements are for a health lifestyle not bodybuilding.

Industry/Entity Type

Health And Wellness

Colors
3176b5
3276b5
33a6d7
85cae6
85abd2
cedeed
e4daeb
b7a5cd

Requirements
Must have
• There will be some text and wording that I will provide that must be on the bottles.

```html
<!DOCTYPE html>
<html lang="en">
<head>
<meta charset="utf-8">
<title>QZN Supplements — Velmora Rest Label</title>
<link rel="stylesheet" href="https://fonts.googleapis.com/css2?family=Montserrat:wght@200;300;500;600;800&display=swap">
<style>
  :root {
    --page-bg: #f4f4f6;
    --label-bg: #7b82b9;
    --band-navy: #252a5e;
    --accent-green: #b7d84c;
    --text-white: #ffffff;
    --icon-tone: #989fcb;
  }
  html, body {
    margin: 0;
    padding: 0;
    width: 1200px;
    height: 984px;
    overflow: hidden;
    background: var(--page-bg);
  }
  .canvas {
    position: relative;
    width: 1200px;
    height: 984px;
  }
  .label {
    position: absolute;
    left: 365px;
    top: 47px;
    width: 470px;
    height: 890px;
    background: var(--label-bg);
    overflow: hidden;
    font-family: "Montserrat", sans-serif;
    color: var(--text-white);
    text-align: center;
  }
  .brand {
    position: absolute;
    top: 68px;
    left: 0;
    width: 100%;
    height: 58px;
    display: flex;
    align-items: center;
    justify-content: center;
    gap: 14px;
  }
  .brand-dot {
    width: 52px;
    height: 52px;
    border-radius: 50%;
    background: var(--accent-green);
    flex: none;
  }
  .brand-name {
    font-weight: 800;
    font-size: 29px;
    letter-spacing: 0.5px;
    white-space: nowrap;
  }
  .product-name {
    position: absolute;
    top: 190px;
    left: 0;
    width: 100%;
    margin: 0;
    font-weight: normal;
  }
  .product-name .line-bold {
    display: block;
    font-weight: 800;
    font-size: 50px;
    line-height: 62px;
    letter-spacing: 1px;
  }
  .product-name .line-light {
    display: block;
    font-weight: 300;
    font-size: 94px;
    line-height: 98px;
    letter-spacing: 2px;
  }
  .product-icon {
    position: absolute;
    top: 384px;
    left: 187px;
    width: 96px;
    height: 96px;
    border-radius: 50%;
    background: var(--icon-tone);
  }
  .benefits {
    position: absolute;
    top: 506px;
    left: 0;
    width: 100%;
    margin: 0;
    padding: 0;
    list-style: none;
    font-weight: 500;
    font-size: 20px;
    line-height: 32px;
  }
  .claims-band {
    position: absolute;
    top: 627px;
    left: 0;
    width: 100%;
    height: 102px;
    background: var(--band-navy);
    color: var(--accent-green);
    font-weight: 500;
    font-size: 22px;
    line-height: 31px;
    display: flex;
    flex-direction: column;
    justify-content: center;
  }
  .net-content {
    position: absolute;
    top: 770px;
    left: 0;
    width: 100%;
    font-weight: 600;
    font-size: 16px;
    line-height: 20px;
  }
  .supplement-type {
    position: absolute;
    top: 808px;
    left: 0;
    width: 100%;
    font-weight: 600;
    font-size: 15px;
    line-height: 20px;
    letter-spacing: 3px;
  }
</style>
</head>
<body>
<div class="canvas">
  <section class="label">
    <div class="brand">
      <span class="brand-dot"></span>
      <span class="brand-name">QZN SUPPLEMENTS</span>
    </div>

    <h1 class="product-name">
      <span class="line-bold">VELMORA</span>
      <span class="line-light">REST</span>
    </h1>

    <div class="product-icon" role="img" aria-label="Line icon of a brain"></div>

    <ul class="benefits">
      <li>NATURAL SLEEP AID</li>
      <li>RESET YOUR CIRCADIAN RHYTHM</li>
      <li>BOOST IMMUNE SYSTEM</li>
    </ul>

    <div class="claims-band">
      <span>NON-GMO | GLUTEN FREE</span>
      <span>SUGAR FREE | VEGAN</span>
    </div>

    <div class="net-content">32 oz</div>
    <div class="supplement-type">DIETARY SUPPLEMENT</div>
  </section>
</div>
</body>
</html>
```